Capability statement graphic design documement

We have written a capability statement for our training business, we would like someone to really make it professional and stand out.

Target Market(s)

Engineering, ports and mining companies

Industry/Entity Type

Coal Mining

Font styles to use
Sans Serif

Colors
9bcb3c

Requirements
Must have
• Very good visual designs.
I have included a couple of example such as the Orvo Dune capability statement which has good designs.
Our colours are green, black, white, grey. Our logos are uploaded.

```html
<!DOCTYPE html>
<html lang="en">
<head>
<meta charset="utf-8">
<title>Capability Statement – Kestrel High Risk Training</title>
<link rel="stylesheet" href="https://fonts.googleapis.com/css2?family=Montserrat:wght@200;300;500;700;800&display=swap">
<style>
  :root {
    --brand-green: #9bcb3c;
    --ink-grey: #58595b;
    --mid-grey: #8a8b8d;
    --light-grey: #ececec;
    --paper: #ffffff;
  }
  * { margin: 0; padding: 0; box-sizing: border-box; }
  html, body { width: 849px; height: 1200px; overflow: hidden; background: var(--paper); }
  .cover {
    position: relative;
    width: 849px;
    height: 1200px;
    overflow: hidden;
    background: var(--paper);
    font-family: "Montserrat", Arial, sans-serif;
  }
  .cover__backdrop {
    position: absolute;
    inset: 0;
    width: 100%;
    height: 100%;
  }
  .brand {
    position: absolute;
    top: 40px;
    right: 44px;
    display: flex;
    flex-direction: column;
    align-items: center;
    gap: 12px;
  }
  .brand__dot {
    width: 84px;
    height: 84px;
    border-radius: 50%;
    background: var(--brand-green);
  }
  .brand__name {
    font-weight: 700;
    font-size: 17px;
    line-height: 1.2;
    letter-spacing: 0.04em;
    text-transform: uppercase;
    text-align: center;
    color: var(--brand-green);
  }
  .title {
    position: absolute;
    left: 84px;
    top: 228px;
    text-transform: uppercase;
    line-height: 1;
  }
  .title__lead {
    display: block;
    font-weight: 800;
    font-size: 70px;
    letter-spacing: 0.01em;
    color: var(--brand-green);
  }
  .title__sub {
    display: block;
    margin-top: 6px;
    font-weight: 200;
    font-size: 66px;
    letter-spacing: 0.02em;
    color: var(--ink-grey);
  }
  .site-link {
    position: absolute;
    left: 42px;
    bottom: 26px;
    font-size: 18px;
    font-weight: 500;
    color: var(--brand-green);
    text-decoration: none;
  }
  .site-link strong { font-weight: 700; }
  .site-link span { color: var(--mid-grey); }
</style>
</head>
<body>
<main class="cover">
  <svg class="cover__backdrop" viewBox="0 0 596 842" preserveAspectRatio="none" aria-hidden="true">
    <defs>
      <linearGradient id="mistGrad" x1="0" y1="0" x2="1" y2="1">
        <stop offset="0" stop-color="#f4f4f4"/>
        <stop offset="1" stop-color="#e4e4e4"/>
      </linearGradient>
      <linearGradient id="bandGrad" x1="0" y1="0" x2="1" y2="0">
        <stop offset="0" stop-color="#e2e2e2"/>
        <stop offset="1" stop-color="#f7f7f7"/>
      </linearGradient>
      <linearGradient id="slateGrad" x1="0" y1="0" x2="1" y2="0">
        <stop offset="0" stop-color="#3a3b3d"/>
        <stop offset="1" stop-color="#9a9b9d"/>
      </linearGradient>
      <linearGradient id="coalGrad" x1="0" y1="0" x2="1" y2="1">
        <stop offset="0" stop-color="#6d6e70"/>
        <stop offset="0.5" stop-color="#2e2f31"/>
        <stop offset="1" stop-color="#1a1a1b"/>
      </linearGradient>
      <linearGradient id="greenRockGrad" x1="0" y1="0" x2="1" y2="1">
        <stop offset="0" stop-color="#4f8f1e"/>
        <stop offset="0.5" stop-color="#2f6a12"/>
        <stop offset="1" stop-color="#143008"/>
      </linearGradient>
      <linearGradient id="cornerGrad" x1="0" y1="1" x2="1" y2="0">
        <stop offset="0" stop-color="#3c3d3f"/>
        <stop offset="1" stop-color="#b5b6b8"/>
      </linearGradient>
    </defs>

    <polygon class="backdrop-mist" points="360,0 596,0 596,150 420,40" fill="url(#mistGrad)"/>
    <polygon class="backdrop-mist" points="0,110 596,230 596,330 0,200" fill="#f6f6f6"/>
    <polygon class="backdrop-band" points="0,272 596,395 596,335 0,232" fill="url(#bandGrad)"/>
    <polygon class="backdrop-band" points="175,345 596,405 596,410 175,380" fill="#e9e9e9"/>

    <polygon class="accent-green" points="0,338 175,380 0,382" fill="#9bcb3c"/>
    <polygon class="accent-slate" points="0,382 175,380 175,445 0,422" fill="url(#slateGrad)"/>

    <polygon points="0,420 285,490 285,765 0,765" fill="url(#coalGrad)" role="img" aria-label="Close-up photograph of raw coal lumps"/>
    <polygon points="285,490 596,405 596,690 330,765 285,765" fill="url(#greenRockGrad)" role="img" aria-label="Close-up photograph of coal lumps tinted brand green"/>

    <polygon class="accent-corner" points="320,768 596,688 596,772" fill="url(#cornerGrad)"/>
  </svg>

  <div class="brand">
    <span class="brand__dot" aria-hidden="true"></span>
    <p class="brand__name">Kestrel<br>High Risk Training</p>
  </div>

  <h1 class="title">
    <span class="title__lead">Capability</span>
    <span class="title__sub">Statement</span>
  </h1>

  <a class="site-link" href="#">www.<strong>kestrelhrt</strong><span>.com.au</span></a>
</main>
</body>
</html>
```